Volunteer Marketplace Needs New Look - www.Brimsey.org

Brimsey is the first online marketplace that lets you buy or sell volunteered services to raise money for charity. (www.Brimsey.org)

We went into live testing a few months ago to get some feedback and feel we need to redo the design. Some points:

- The current design was developed when a previous logo was being used. We later developed the current logo (which we love) and have never felt it really fit into the design. A design that plays up the logo would be great but not required.

- The circles in the logo represent coins which is a theme we are using in our branding (our business cards are coins). The marketplace offers a new form of currency people can use to give back. We don't feel the design should center around this concept, but a small element would be a nice touch.

We want a design that is engaging and fun - but still professional and credible.
Updates

I just want to thank you all for submitting designs. I have been trying to send feedback to everyone and am starting to eliminate designs so I can begin to narrow it. It is so hard to decide. You all did a great job! 

Target Market(s)

There are three target audiences - volunteers donating their services, customers buying donated services, and charities joining the program.

Industry/Entity Type

Business

Requirements
Must have
• - We feel we need to represent on the home page the concept of there being two parties that are coming together - the Volunteer and the Customer.

- We have a 60 second overview video in the works that we would like displayed on the home page.
Nice to have
• Incase it is helpful, here are some designs we like - but please know we are looking for creative ideas. Your design does not have to look like these.

http://www.lendora.org/
https://www.taskwell.com/
http://www.layoutbarn.com/website-templates/40056.html
http://www.layoutbarn.com/website-templates/40121.html
http://www.craftpool.com/

Also - please be creative about what content we put on our home page. We want to modernize the site. We can feed in our blog, twitter, facebook, etc into the home page if you think we should. We need your expertise to recommend what we need to showcase.
Should not have
• Please note that the paragraphs of content do not have to be on the home page. These are there now, but feedback tells us it is too boring - and they is why we are having the video done. So - you do not have to make room for all that text.

```html
<!DOCTYPE html>
<html lang="en">
<head>
<meta charset="utf-8">
<title>Brimsey</title>
<link rel="stylesheet" href="https://fonts.googleapis.com/css2?family=Arimo:wght@400;700&family=Comic+Neue:wght@400;700&display=swap">
<style>
  :root{
    --page-bg:#e8e8e8;
    --header-bg:#f5f5f5;
    --rule-dark:#4a5560;
    --rule-teal:#2a7f95;
    --link-teal:#2a7490;
    --brand-slate:#4a5a6c;
    --green:#8bcb57;
    --green-light:#a6d978;
    --green-dark:#84c34c;
    --panel-dark:#424242;
    --panel-mid:#4b4b4b;
    --text-body:#55574f;
    --text-nav:#333;
    --footer-text:#5b5f66;
    --white:#fff;
  }
  *{box-sizing:border-box;margin:0;padding:0}
  html,body{width:1200px;height:900px;overflow:hidden}
  body{position:relative;background:var(--page-bg);font-family:"Arimo",Arial,sans-serif}
  .site-header{position:absolute;left:0;top:0;width:1200px;height:188px;background:var(--header-bg);border-top:1px solid var(--rule-teal);border-bottom:1px solid var(--rule-dark)}
  .brand-name{position:absolute;left:120px;top:40px;font-family:"Arimo",Arial,sans-serif;font-weight:700;font-size:96px;line-height:110px;color:var(--brand-slate);letter-spacing:-1px}
  .search-box{position:absolute;left:799px;top:33px;width:125px;height:24px;border:1px solid #b9b9b9;border-radius:4px;background:#fafafa;box-shadow:inset 0 1px 2px #ccc}
  .search-box svg{position:absolute;right:4px;top:4px}
  .account-link{position:absolute;top:35px;font-size:15px;color:var(--link-teal);text-decoration:none}
  .join-us{position:absolute;left:981px;top:68px;font-size:12px;color:#444}
  .social{position:absolute;top:90px;width:15px;height:15px;border-radius:2px}
  .main-nav{position:absolute;left:589px;top:133px;width:483px;height:38px;border-top:1px solid var(--green);border-bottom:1px solid var(--green)}
  .nav-item{position:absolute;top:0;height:36px;line-height:36px;font-size:14px;color:var(--text-nav);text-decoration:none;white-space:nowrap;letter-spacing:-.2px}
  .nav-item.is-active{left:0;width:183px;text-align:center;background:var(--green);color:var(--white);border-radius:5px 0 0 0;top:-2px;height:39px;line-height:39px}
  .nav-item.is-last{right:0}
  .welcome-panel{position:absolute;left:123px;top:275px;width:954px;height:456px;border:1px solid #fff;background:linear-gradient(var(--green-dark),var(--green-light) 55%,var(--green-dark));box-shadow:0 0 3px rgba(0,0,0,.2)}
  .welcome-title{position:absolute;left:72px;top:95px;font-family:"Comic Neue",cursive;font-size:33px;color:var(--white);font-weight:700}
  .welcome-text{position:absolute;left:70px;top:148px;width:335px;font-family:"Comic Neue",cursive;font-weight:700;font-size:15px;line-height:18.3px;color:var(--text-body)}
  .read-more{position:absolute;left:302px;top:320px;width:87px;height:23px;background:#d2d2d2;border:1px solid #7a7a7a;font-size:14px;color:#222;text-align:center;line-height:21px}
  .community-panel{position:absolute;left:589px;top:259px;width:436px;height:492px;background:var(--panel-dark);border:2px solid var(--white)}
  .member-photo{position:absolute}
  .video-card{position:absolute;left:25px;top:292px;width:383px;height:172px;background:var(--panel-mid);border:1px solid #575757;border-radius:3px;box-shadow:0 0 4px rgba(0,0,0,.4)}
  .video-player{position:absolute;left:17px;top:11px;width:280px;height:150px;border:3px solid #9c9c9c;background:#000}
  .video-frame{position:absolute;left:30px;top:3px;width:214px;height:123px;background:radial-gradient(#8a9294,#3f4749)}
  .video-controls{position:absolute;left:0;bottom:0;width:274px;height:18px;background:#1b1b1b}
  .video-thumb{position:absolute;left:307px;width:56px;height:36px;border:2px solid #9c9c9c}
  .footer-nav{position:absolute;left:0;top:803px;width:1200px;text-align:center;font-size:15px;color:var(--footer-text)}
  .footer-nav a{color:var(--footer-text);text-decoration:none}
  .footer-nav .sep{margin:0 9px;font-size:13px}
</style>
</head>
<body>
<header class="site-header">
  <div class="brand-name">Brimsey</div>
  <div class="search-box">
    <svg width="14" height="14" viewBox="0 0 14 14"><circle cx="6" cy="6" r="4" fill="none" stroke="#6a7fa8" stroke-width="1.5"/><line x1="9" y1="9" x2="13" y2="13" stroke="#6a7fa8" stroke-width="2"/></svg>
  </div>
  <a class="account-link" style="left:951px" href="#">Log in</a>
  <a class="account-link" style="left:1017px" href="#">Register</a>
  <div class="join-us">Join us</div>
  <span class="social" style="left:974px;background:#3b5b9a" aria-label="Social network"></span>
  <span class="social" style="left:997px;background:#5fb6d9" aria-label="Social network"></span>
  <span class="social" style="left:1018px;background:#e07a2c" aria-label="News feed"></span>
  <nav class="main-nav">
    <a class="nav-item is-active" href="#">Search donated service</a>
    <a class="nav-item" style="left:211px" href="#">Search help wanted ads</a>
    <a class="nav-item is-last" href="#">How it works</a>
  </nav>
</header>

<section class="welcome-panel">
  <h1 class="welcome-title">WELCOME!</h1>
  <p class="welcome-text">Lorem ipsum dolor,<br>consectetuer adipiscing elit. Aenean commodo ligula eget dolor. Aenean massa. Cum sociis na-toque penat.<br>si. Aenean vulputate eleifend Phasellus viverra nulla ut metus varius laoreet.Quisque.<br>si. Aenean vulputate eleifend Phasellus viverra nulla ut metus varius laoreet.Quisque.</p>
  <div class="read-more">read more</div>
</section>

<section class="community-panel">
  <div class="member-photo" role="img" aria-label="Volunteer portrait" style="left:24px;top:14px;width:85px;height:118px;background:linear-gradient(#b9b2a6,#d8dce2)"></div>
  <div class="member-photo" role="img" aria-label="Volunteer portrait" style="left:122px;top:14px;width:85px;height:118px;background:linear-gradient(#5d5a45,#7b5d55)"></div>
  <div class="member-photo" role="img" aria-label="Volunteer portrait" style="left:219px;top:17px;width:85px;height:118px;background:linear-gradient(#4a4038,#2a2624)"></div>
  <div class="member-photo" role="img" aria-label="Volunteer portrait" style="left:319px;top:14px;width:88px;height:118px;background:linear-gradient(#d6d0c8,#5b5a58)"></div>
  <div class="member-photo" role="img" aria-label="Customer portrait" style="left:24px;top:146px;width:86px;height:117px;background:linear-gradient(#8a5c54,#6d4c47)"></div>
  <div class="member-photo" role="img" aria-label="Customer portrait" style="left:122px;top:146px;width:85px;height:117px;background:linear-gradient(#6a5a48,#c4cad0)"></div>
  <div class="member-photo" role="img" aria-label="Customer portrait" style="left:220px;top:146px;width:85px;height:117px;background:linear-gradient(#6a5648,#2a2220)"></div>
  <div class="member-photo" role="img" aria-label="Customer portrait" style="left:319px;top:146px;width:88px;height:117px;background:linear-gradient(#3e4a30,#b49070)"></div>
  <div class="video-card">
    <div class="video-player" role="img" aria-label="Overview video: two hands joining">
      <div class="video-frame"></div>
      <svg style="position:absolute;left:116px;top:45px" width="46" height="26" viewBox="0 0 46 26"><rect x="1" y="1" width="44" height="24" rx="5" fill="#c9d2d4" fill-opacity=".85"/><polygon points="18,7 30,13 18,19" fill="#3f4a50"/></svg>
      <div class="video-controls">
        <svg width="274" height="18" viewBox="0 0 274 18"><rect x="0" y="1" width="274" height="3" fill="#444"/><rect x="0" y="1" width="195" height="3" fill="#c51a1a"/><circle cx="195" cy="2.5" r="3" fill="#eee"/><polygon points="9,8 9,15 15,11.5" fill="#ccc"/><rect x="24" y="9" width="6" height="5" fill="#ccc"/></svg>
      </div>
    </div>
    <div class="video-thumb" role="img" aria-label="Video thumbnail" style="top:23px;background:linear-gradient(#222,#777)"></div>
    <div class="video-thumb" role="img" aria-label="Video thumbnail" style="top:66px;background:linear-gradient(#555,#aaa)"></div>
    <div class="video-thumb" role="img" aria-label="Video thumbnail" style="top:110px;background:linear-gradient(#111,#888)"></div>
  </div>
</section>

<footer class="footer-nav">
  <a href="#">Home</a><span class="sep">I</span><a href="#">Newsroom</a><span class="sep">I</span><a href="#">About Brimsey</a><span class="sep">I</span> <a href="#">Charities</a> <span class="sep">I</span><a href="#">Contact Brimsey</a>
</footer>
</body>
</html>
```